Pest control truck wrap

Needing an eye catching wrap for my new work truck. Its a 2018 Varenko Bellwick SR Access Cab with a Dunmar 240vkt canopy. It needs to stand out and be eye catching but not too busy, I want people to know who I am and what I'm doing. It also needs to be easily adaptable to my older trucks, which are full size without canopies. I prefer solid colors, probably black, white and green, and maybe a little orange. My logo should be large enough that it can be easily read from a distance, but not so big it takes up the whole truck. Since this is a pest control truck, it should communicate that. Bear in mind we primarily do insect and spider control, not rodents or wildlife. I'll include photos of the new truck, my logo, and one of my older trucks for reference.

```html
<!DOCTYPE html>
<html lang="en">
<head>
<meta charset="utf-8">
<title>Kestrel Weed and Pest Control — Truck Wrap</title>
<link rel="stylesheet" href="https://fonts.googleapis.com/css2?family=Anton&family=Exo+2:ital,wght@1,800&family=Russo+One&display=swap">
<style>
  :root {
    --wrap-white: #ffffff;
    --wrap-black: #111111;
    --wrap-green: #1f9a3c;
    --wrap-orange: #f0922f;
    --wrap-orange-deep: #e47a17;
    --ring-grey: #9a9a9a;
    --page-bg: #f2f2f2;
  }
  html, body {
    margin: 0;
    width: 1200px;
    height: 1200px;
    overflow: hidden;
    background: var(--page-bg);
  }
  .canvas {
    width: 1200px;
    height: 1200px;
    display: flex;
    flex-direction: column;
    align-items: center;
    justify-content: center;
    gap: 90px;
  }
  .side-panel { width: 1100px; height: 420px; display: block; box-shadow: 0 6px 18px rgba(0,0,0,.12); }
  .tailgate-panel { width: 800px; height: 280px; display: block; box-shadow: 0 6px 18px rgba(0,0,0,.12); }
  .brand-name { font-family: "Anton", sans-serif; fill: var(--wrap-black); }
  .brand-tagline { font-family: "Anton", sans-serif; fill: var(--wrap-black); letter-spacing: 1px; }
  .phone { font-family: "Russo One", sans-serif; fill: var(--wrap-black); }
  .service-line { font-family: "Exo 2", sans-serif; font-style: italic; font-weight: 800; fill: var(--wrap-white); letter-spacing: 1px; }
</style>
</head>
<body>
<main class="canvas">

  <!-- Side of truck -->
  <svg class="side-panel" viewBox="0 0 1100 420" aria-label="Side wrap layout">
    <rect width="1100" height="420" fill="var(--wrap-white)"/>

    <!-- rear colour block -->
    <rect class="band-orange" x="600" y="90" width="500" height="70" fill="var(--wrap-orange)"/>
    <rect class="band-green" x="600" y="160" width="500" height="200" fill="var(--wrap-green)"/>

    <!-- lower speed stripes -->
    <g class="speed-stripes">
      <polygon points="80,300 110,300 150,345 120,345" fill="var(--wrap-green)"/>
      <polygon points="120,300 150,300 190,345 160,345" fill="var(--wrap-orange-deep)"/>
      <polygon points="165,300 195,300 235,345 205,345" fill="var(--wrap-green)"/>
      <polygon points="210,300 240,300 280,345 250,345" fill="var(--wrap-orange-deep)"/>
      <polygon points="255,300 285,300 325,345 295,345" fill="var(--wrap-orange-deep)"/>
      <polygon points="330,300 480,300 520,265 600,265 600,345 360,345" fill="var(--wrap-orange-deep)"/>
    </g>

    <!-- mark circle -->
    <circle cx="598" cy="215" r="125" fill="var(--wrap-white)" stroke="var(--ring-grey)" stroke-width="4"/>
    <circle cx="598" cy="215" r="114" fill="var(--wrap-white)" stroke="var(--wrap-black)" stroke-width="11"/>

    <!-- name -->
    <text class="brand-tagline" x="455" y="150" font-size="20" text-anchor="end">Weed and Pest Control</text>
    <text class="brand-name" x="70" y="265" font-size="118" textLength="385" lengthAdjust="spacingAndGlyphs">Kestrel</text>

    <!-- contact -->
    <text class="phone" x="1065" y="142" font-size="40" text-anchor="end">(555) 014 2287</text>
    <text class="service-line" x="1065" y="198" font-size="24" text-anchor="end">INSECT &amp; SPIDER CONTROL</text>
  </svg>

  <!-- Tailgate -->
  <svg class="tailgate-panel" viewBox="0 0 800 280" aria-label="Tailgate wrap layout">
    <rect width="800" height="280" fill="var(--wrap-orange)"/>
    <polygon class="band-green" points="0,0 730,0 640,125 0,125" fill="var(--wrap-green)"/>
    <rect class="band-green" x="0" y="150" width="220" height="130" fill="var(--wrap-green)"/>

    <circle cx="185" cy="140" r="128" fill="var(--wrap-white)" stroke="var(--ring-grey)" stroke-width="4"/>
    <circle cx="185" cy="140" r="117" fill="var(--wrap-white)" stroke="var(--wrap-black)" stroke-width="11"/>

    <text class="service-line" x="760" y="55" font-size="28" text-anchor="end">INSECT &amp; SPIDER CONTROL</text>
    <text class="brand-tagline" x="745" y="155" font-size="20" text-anchor="end">Weed and Pest Control</text>
    <text class="brand-name" x="385" y="250" font-size="100" textLength="360" lengthAdjust="spacingAndGlyphs">Kestrel</text>
  </svg>

</main>
</body>
</html>
```